brightmesh Business Card

Already have the logo, but now need the business card design

Industry/Entity Type

Business Software

Contact Information for Business Card

web site will be brightmesh.io / The card should have the person name / position / mobile / email / and company address

Colors

Designer to choose colors to be used in the design.

Requirements
Must have
• See business card details
• One side to have the brightmesh logo
Nice to have
• If possible the 'O' from flow can be watermarked into the second side
• Try to fit in the words brightmesh Business Solutions

```html
<!DOCTYPE html>
<html lang="en">
<head>
<meta charset="UTF-8">
<title>brightmesh Business Card</title>
<link href="https://fonts.googleapis.com/css2?family=Arimo:wght@400;700&family=Questrial&display=swap" rel="stylesheet">
<style>
  :root {
    --page-bg: #e6e6e6;
    --card-bg: #ffffff;
    --ink-grey: #6f6f6f;
    --ink-dark: #5a5a5a;
    --accent-red: #e8202a;
    --card-shadow: rgba(0, 0, 0, 0.18);
  }
  html, body {
    margin: 0;
    padding: 0;
    overflow: hidden;
  }
  body {
    width: 1200px;
    height: 880px;
    background: var(--page-bg);
    position: relative;
    font-family: "Arimo", Arial, sans-serif;
  }
  .card {
    position: absolute;
    left: 290px;
    width: 620px;
    height: 354px;
    background: var(--card-bg);
    border-radius: 22px;
    box-shadow: 0 8px 24px var(--card-shadow);
    overflow: hidden;
  }
  .card--front { top: 70px; }
  .card--back { top: 456px; }

  .brand {
    position: absolute;
    left: 0;
    right: 0;
    top: 118px;
    text-align: center;
  }
  .brand__name {
    font-family: "Questrial", "Century Gothic", sans-serif;
    font-size: 78px;
    color: var(--ink-grey);
    letter-spacing: -1px;
    line-height: 1;
  }
  .brand__web {
    margin-top: 6px;
    padding-left: 230px;
    font-size: 15px;
    color: var(--accent-red);
    letter-spacing: 0.5px;
  }

  .contact {
    position: absolute;
    left: 58px;
    top: 118px;
    color: var(--ink-grey);
    font-size: 15px;
    line-height: 1.3;
  }
  .contact__name {
    font-size: 22px;
    font-weight: 700;
    color: var(--ink-dark);
    line-height: 1.05;
  }
  .contact__role {
    font-size: 16px;
    color: var(--accent-red);
    margin-bottom: 10px;
  }
  .contact__address { margin-bottom: 8px; }
  .contact__row {
    display: flex;
    align-items: center;
    gap: 8px;
  }
  .contact__row svg { flex: none; }
  .contact__web {
    margin-top: 12px;
    font-size: 16px;
    letter-spacing: 0.5px;
  }
  .contact__web .accent { color: var(--accent-red); }

  .back-brand {
    position: absolute;
    right: 46px;
    top: 72px;
    font-family: "Questrial", "Century Gothic", sans-serif;
    font-size: 44px;
    color: var(--ink-grey);
  }
</style>
</head>
<body>
  <section class="card card--front">
    <div class="brand">
      <div class="brand__name">brightmesh</div>
      <div class="brand__web">www.brightmesh.io</div>
    </div>
  </section>

  <section class="card card--back">
    <div class="back-brand">brightmesh</div>
    <div class="contact">
      <div class="contact__name">Liam Carter</div>
      <div class="contact__role">Founder</div>
      <div class="contact__address">PO BOX 418 Kestrel Lane<br>7 Ashford Road Perth</div>
      <div class="contact__row">
        <svg width="18" height="18" viewBox="0 0 18 18" aria-hidden="true">
          <circle cx="9" cy="9" r="8" fill="none" stroke="#e8202a" stroke-width="1.6"/>
          <path d="M6 5.2 L7.4 5 L8.2 7 L7.3 7.8 Q8 9.6 10 10.6 L10.9 9.7 L12.9 10.6 L12.7 12 Q10.2 12.6 7.8 10.3 Q5.5 8 6 5.2 Z" fill="#e8202a"/>
        </svg>
        <span>(555) 018-2437</span>
      </div>
      <div class="contact__row">
        <svg width="18" height="18" viewBox="0 0 18 18" aria-hidden="true">
          <circle cx="9" cy="9" r="8" fill="none" stroke="#e8202a" stroke-width="1.6"/>
          <rect x="5" y="6" width="8" height="6" fill="#e8202a"/>
          <path d="M5 6 L9 9.5 L13 6" fill="none" stroke="#ffffff" stroke-width="1"/>
        </svg>
        <span>hello@brightmesh.io</span>
      </div>
      <div class="contact__web">www.<span class="accent">brightmesh</span>.io</div>
    </div>
  </section>
</body>
</html>
```